New Website for novelty yarn producer

We need a new website for our company, Tarvek. We make highly tailored yarns for weavers worldwide. This year marks our 40th anniversary and we want to evolve our image and identity.

Our temporary website can be found at:
www.tarvekyarns.com

Our only concern in that throughout the website the protagonist must be our client, we make their creations possible and are highly adaptable both during the ideation process of the yarn as well as in the production. This is at the core of the way we do business and is summarised within the concept of FPM (Fluid Partner Method).

Industry/Entity Type

Textile

Number of Pages Required

1 page

Colors
9bcb3c

Requirements
Must have
• Fluid Partner Method (FPM) - can be found on or current website www.tarvekyarns.com

```html
<!DOCTYPE html>
<html lang="en">
<head>
<meta charset="utf-8">
<title>Tarvek – Novelty Yarn Solutions</title>
<link href="https://fonts.googleapis.com/css2?family=Libre+Baskerville:wght@400;700&family=Gelasio:wght@400;600&display=swap" rel="stylesheet">
<style>
:root{
  --green:#9bcb3c;
  --text:#333333;
  --heading:#444444;
  --muted:#8a8a8a;
  --rule:#c4c4c4;
  --paper:#ffffff;
  --panel:#f1f1f1;
  --pink:#e5336f;
  --hero-a:#2a2624;
  --hero-b:#5a4a40;
}
*{margin:0;padding:0;box-sizing:border-box}
html,body{width:1200px;height:2190px;overflow:hidden;background:var(--paper)}
body{font-family:"Gelasio",Georgia,serif;color:var(--text);position:relative}
.heading{font-family:"Libre Baskerville",Georgia,serif;font-weight:400;color:var(--heading);text-transform:uppercase}
.btn{position:absolute;left:50%;transform:translateX(-50%);display:inline-block;background:var(--green);color:#fff;font-family:"Libre Baskerville",Georgia,serif;font-weight:700;font-size:14px;line-height:16px;text-transform:uppercase;padding:11px 16px;box-shadow:2px 3px 4px rgba(0,0,0,.25);text-decoration:none;white-space:nowrap}

/* header */
.site-header{position:absolute;top:0;left:0;width:1200px;height:108px}
.contact-item{position:absolute;top:20px;display:flex;align-items:center;gap:14px;font-size:13px;color:var(--text)}
.contact-item.phone{left:150px}
.contact-item.mail{left:875px}
.brand{position:absolute;top:18px;left:0;width:1200px;text-align:center;font-family:"Libre Baskerville",Georgia,serif;font-size:52px;color:#111;letter-spacing:1px}
.rule{position:absolute;left:0;width:1200px;height:1px;background:var(--rule)}
.rule.top{top:112px}
.rule.bottom{top:146px}
.main-nav{position:absolute;top:122px;left:0;width:1200px;display:flex;justify-content:center;font-size:13px;text-transform:uppercase;color:var(--text)}
.main-nav a{color:inherit;text-decoration:none;padding:0 19px;position:relative}
.main-nav a+a::before{content:"";position:absolute;left:-3px;top:6px;width:5px;height:5px;border-radius:50%;background:var(--text)}
.main-nav a.current{color:var(--green)}

/* hero */
.hero{position:absolute;top:159px;left:0;width:1200px;height:450px;background:radial-gradient(ellipse at 50% 55%,var(--hero-b) 0%,#3b332e 45%,var(--hero-a) 100%);text-align:center;color:#fff}
.anniversary{position:absolute;top:77px;left:545px;width:110px;height:110px;border:1.5px solid rgba(255,255,255,.85);border-radius:50%;font-family:"Libre Baskerville",Georgia,serif;font-size:42px;line-height:106px}
.hero-title{position:absolute;top:218px;width:100%;font-family:"Libre Baskerville",Georgia,serif;font-weight:700;font-size:34px;letter-spacing:1px;color:#fff}
.hero .btn{top:288px}

/* section title with plain rules */
.titled{position:absolute;left:150px;width:900px;display:flex;align-items:center;gap:12px}
.titled .line{flex:1;height:1px;background:var(--rule)}
.titled h2{font-size:22px;white-space:nowrap}

.welcome{position:absolute;top:609px;left:0;width:1200px;height:286px;text-align:center}
.welcome .titled{top:32px}
.welcome p{width:610px;margin:0 auto;font-size:13.5px;line-height:20px}
.welcome .lead{margin-top:92px}
.welcome .lead+p{margin-top:20px}
.welcome .btn{top:210px}

.why{position:absolute;top:895px;left:0;width:1200px;height:322px;background:var(--panel);text-align:center}
.why h2{margin-top:32px;font-size:22px}
.features{display:flex;justify-content:center;margin-top:30px}
.feature{width:342px}
.feature .icon{width:78px;height:78px;border-radius:50%;margin:0 auto;background:var(--green);border:3px solid var(--pink)}
.feature h3{font-weight:400;font-size:14px;margin-top:12px}
.feature h3::after{content:"";display:block;width:38px;height:3px;border-top:1px solid var(--green);border-bottom:1px solid var(--green);margin:9px auto 10px}
.feature p{font-size:12.5px;line-height:16px;width:215px;margin:0 auto}

.production{position:absolute;top:1217px;left:0;width:1200px;height:426px;text-align:center}
.production .titled{top:32px}
.method-mark{position:absolute;top:90px;left:435px;display:flex;align-items:center;gap:26px}
.method-mark .dot{width:110px;height:110px;border-radius:50%;border:3px solid var(--green)}
.method-mark .divider{width:2px;height:120px;background:#111}
.method-mark .name{font-family:"Libre Baskerville",Georgia,serif;font-size:26px;line-height:32px;text-align:left;color:#111;text-transform:uppercase}
.production p{position:absolute;top:250px;left:295px;width:610px;font-size:14px;line-height:20px}
.production .btn{top:350px}

.numbers{position:absolute;top:1643px;left:0;width:1200px;height:299px;background:linear-gradient(100deg,#1e1e1e 0%,#3c3c3c 45%,#2a2a2a 100%);color:#fff;text-align:center}
.numbers h2{margin-top:30px;font-size:21px;color:#fff;font-weight:700}
.stats{display:flex;justify-content:center;margin-top:26px}
.stat{width:268px}
.stat .ring{width:68px;height:68px;border-radius:50%;border:1.5px solid #fff;margin:0 auto;font-family:"Libre Baskerville",Georgia,serif;font-size:32px;line-height:64px}
.stat span{display:block;margin-top:10px;font-size:14px;font-weight:600}
.numbers .btn{top:224px}

.site-footer{position:absolute;top:1942px;left:0;width:1200px;height:248px;background:var(--panel);font-size:11.5px}
.footer-brand{position:absolute;top:36px;left:150px;font-family:"Libre Baskerville",Georgia,serif;font-size:42px;color:#111}
.footer-col h4{font-family:"Libre Baskerville",Georgia,serif;font-weight:700;font-size:14px;text-transform:uppercase;margin-bottom:14px}
.links{position:absolute;top:40px;left:366px}
.links ul{list-style:none}
.links li{margin-bottom:8px}
.reach{position:absolute;top:40px;left:540px}
.reach .row{display:flex;gap:14px;align-items:flex-start;margin-bottom:14px;line-height:13px}
.reach .row svg{flex:none}
.legal{position:absolute;top:66px;left:798px;line-height:14px}
.rule.foot{top:2153px;background:#bdbdbd}
.copyright{position:absolute;bottom:0;left:0;width:1200px;height:24px;text-align:center;font-size:9px;color:var(--muted);padding-top:8px;font-family:Arial,sans-serif}
</style>
</head>
<body>

<header class="site-header">
  <div class="contact-item phone">
    <svg width="22" height="22" viewBox="0 0 24 24" aria-hidden="true"><path d="M6.6 10.8a15 15 0 0 0 6.6 6.6l2.2-2.2c.3-.3.7-.4 1-.2 1.1.4 2.3.6 3.6.6.6 0 1 .4 1 1V20c0 .6-.4 1-1 1A17 17 0 0 1 3 4c0-.6.4-1 1-1h3.5c.6 0 1 .4 1 1 0 1.3.2 2.5.6 3.6.1.3 0 .7-.2 1z" fill="none" stroke="#444" stroke-width="1.6"/></svg>
    0555 48210
  </div>
  <div class="brand">TARVEK</div>
  <div class="contact-item mail">
    <svg width="28" height="20" viewBox="0 0 28 20" aria-hidden="true"><rect x="1" y="1" width="26" height="18" fill="#555"/><path d="M1 1l13 10L27 1" fill="none" stroke="#fff" stroke-width="1.5"/></svg>
    sales@tarvekyarns.com
  </div>
</header>
<div class="rule top"></div>
<nav class="main-nav">
  <a class="current" href="#">Home</a><a href="#">About us</a><a href="#">Fluid Partner Method</a><a href="#">Heritage</a><a href="#">Team</a><a href="#">Blog</a><a href="#">Contact</a>
</nav>
<div class="rule bottom"></div>

<section class="hero" role="img" aria-label="Photograph of a skein of multicoloured yarn lying on a dark wooden table">
  <div class="anniversary">40</div>
  <h1 class="hero-title">TAILORED WEAVING SOLUTIONS</h1>
  <a class="btn" href="#">Find out more</a>
</section>

<section class="welcome">
  <div class="titled"><span class="line"></span><h2 class="heading">Welcome to Tarvek Yarn Solutions</h2><span class="line"></span></div>
  <p class="lead">Our team has decades of experience in providing yarn solutions to weavers around the world, assisting them in the creation of outstanding textiles. Our clients can expect open lines of communication, clarity and professionality</p>
  <p>Our focus is our client. The success of a client is our success.</p>
  <a class="btn" href="#">See our heritage</a>
</section>

<section class="why">
  <h2 class="heading">Why choose us</h2>
  <div class="features">
    <div class="feature">
      <div class="icon" role="img" aria-label="Illustration of a ball of yarn"></div>
      <h3>Experience</h3>
      <p>Over the years the company has gained the knowledge and skills that define the superiority of our product and the rigor of our work ethic</p>
    </div>
    <div class="feature">
      <div class="icon" role="img" aria-label="Illustration of a spool of thread"></div>
      <h3>Creativity</h3>
      <p>Our belief is that the key to our clients' success is a combination of innovation, creativity and quality and we strive to meet clients' demands</p>
    </div>
    <div class="feature">
      <div class="icon" role="img" aria-label="Illustration of a wound yarn cone"></div>
      <h3>Professionality</h3>
      <p>We are a family business at the core. Our company is run with the same values as the Ferrani family: respect, determination and commitment.</p>
    </div>
  </div>
</section>

<section class="production">
  <div class="titled"><span class="line"></span><h2 class="heading">Production built around you</h2><span class="line"></span></div>
  <div class="method-mark">
    <span class="dot"></span>
    <span class="divider"></span>
    <span class="name">Fluid<br>Partner<br>Method</span>
  </div>
  <p>Working together with weavers from step one, starting from the desired end product and working backwards. Versatility and flexibility both in development and production are key in delivering a custom solution capable of giving life to your products.</p>
  <a class="btn" href="#">Find out more</a>
</section>

<section class="numbers" role="img" aria-label="Black and white photograph of hands working yarn at a loom">
  <h2 class="heading">TYS in numbers</h2>
  <div class="stats">
    <div class="stat"><div class="ring">40</div><span>Years In Business</span></div>
    <div class="stat"><div class="ring">2</div><span>Million Kilograms/YR</span></div>
    <div class="stat"><div class="ring">8</div><span>Brands</span></div>
  </div>
  <a class="btn" href="#">Find out more</a>
</section>

<footer class="site-footer">
  <div class="footer-brand">TARVEK</div>
  <div class="footer-col links">
    <h4>Quick links</h4>
    <ul><li>Home</li><li>About us</li><li>FPM</li><li>Heritage</li><li>Team</li><li>Blog</li></ul>
  </div>
  <div class="footer-col reach">
    <h4>Contact</h4>
    <div class="row">
      <svg width="16" height="20" viewBox="0 0 16 20" aria-hidden="true"><path d="M8 0a7 7 0 0 0-7 7c0 5 7 13 7 13s7-8 7-13a7 7 0 0 0-7-7z" fill="#444"/><circle cx="8" cy="7" r="2.6" fill="#f1f1f1"/></svg>
      <span>VIA DEI TESSITORI 14,<br>50100 ARVENA, ITALY</span>
    </div>
    <div class="row">
      <svg width="16" height="16" viewBox="0 0 24 24" aria-hidden="true"><path d="M6.6 10.8a15 15 0 0 0 6.6 6.6l2.2-2.2c.3-.3.7-.4 1-.2 1.1.4 2.3.6 3.6.6.6 0 1 .4 1 1V20c0 .6-.4 1-1 1A17 17 0 0 1 3 4c0-.6.4-1 1-1h3.5c.6 0 1 .4 1 1 0 1.3.2 2.5.6 3.6.1.3 0 .7-.2 1z" fill="none" stroke="#444" stroke-width="2"/></svg>
      <span>0555 48210</span>
    </div>
    <div class="row">
      <svg width="16" height="16" viewBox="0 0 16 16" aria-hidden="true"><rect x="4" y="1" width="8" height="5" fill="#444"/><rect x="1" y="6" width="14" height="6" rx="1" fill="#444"/><rect x="4" y="10" width="8" height="5" fill="#f1f1f1" stroke="#444"/></svg>
      <span>0555 48299</span>
    </div>
  </div>
  <div class="legal">
    R.E.A AR 418205 - Reg. Imp. AR 04120338812<br>
    P. IVA 00482150093 - Cod. Fisc. 04120338812<br>
    Capitale sociale € 84.300,00 int. ver.
  </div>
  <div class="copyright">Copyright @ 2018 TarvekNoveltyYarnSolutions. All rights reserved.</div>
</footer>
<div class="rule foot"></div>

</body>
</html>
```